Business card for Velora Homeworks

Hi again, I need a business card for my Velora Homeworks business you have been working on with the following information:

Tessa Quill
Director
m. 0438 276 615
e. tessa@velorahomeworks.com.au
w. www.velorahomeworks.com.au

Maybe you could use the original design (using both the green & white) and where the white box is you could include the above details (name / mobile / etc) - Perhaps the 'i' in Tessa could be the bow tie again?

Then the back could be green with black writing stating:

Services Offered:

* Personal Assistant Concierge
* Decluttering Concierge
* Home Management Concierge
* FIFO Concierge
* Events Concierge
* Leisure & Travel Concierge
* Seasonal Concierge
* Professional Concierge

Many thanks
Updates

Hi Everyone I'm really sorry but I am working with just one designer on this brief, thank you for your work and apologies for my error.

Industry/Entity Type

Business

```html
<!DOCTYPE html>
<html lang="en">
<head>
<meta charset="utf-8">
<title>Velora Homeworks – Business Card</title>
<link rel="stylesheet" href="https://fonts.googleapis.com/css2?family=PT+Sans:wght@400;700&family=Archivo+Black&display=swap">
<style>
  :root {
    --backdrop: #4a4a4c;
    --paper: #ffffff;
    --paper-shade: #e4e4e6;
    --green: #0f9346;
    --green-mid: #39b54a;
    --green-light: #8dc63f;
    --charcoal: #1a1a1a;
    --grey-text: #555555;
    --ink: #111111;
  }
  * { margin: 0; padding: 0; box-sizing: border-box; }
  html, body {
    width: 1200px; height: 999px; overflow: hidden;
    background: var(--backdrop);
  }
  .canvas { position: relative; width: 1200px; height: 999px; }

  .card {
    position: absolute;
    width: 700px; height: 410px;
    border-radius: 26px;
    overflow: hidden;
  }

  /* Front */
  .card-front {
    left: 80px; top: 60px;
    background: linear-gradient(180deg, var(--paper) 0%, var(--paper) 30%, var(--paper-shade) 65%);
  }
  .card-front .sweep { position: absolute; inset: 0; width: 700px; height: 410px; }
  .identity {
    position: absolute; left: 0; top: 62px; width: 560px;
    text-align: center;
    font-family: "PT Sans", sans-serif;
  }
  .identity .name {
    font-weight: 700; font-size: 50px; line-height: 1;
    color: var(--green); letter-spacing: -0.5px;
  }
  .identity .role {
    margin-top: 6px; padding-left: 70px;
    font-size: 29px; color: var(--grey-text);
  }
  .contacts {
    position: absolute; left: 330px; top: 292px;
    list-style: none;
    font-family: "PT Sans", sans-serif;
    font-size: 23px; color: var(--ink);
  }
  .contacts li { display: flex; align-items: center; height: 32px; }
  .contacts svg { width: 18px; height: 18px; margin-right: 12px; flex: none; }

  /* Back */
  .card-back {
    left: 420px; top: 530px;
    background: radial-gradient(ellipse at 50% 50%, var(--green-light) 0%, var(--green-mid) 45%, var(--green) 100%);
  }
  .services { position: absolute; left: 80px; top: 42px; color: var(--ink); }
  .services h2 {
    font-family: "Archivo Black", sans-serif;
    font-weight: 400; font-size: 30px; line-height: 1;
    margin-left: -30px; margin-bottom: 16px;
  }
  .services ul { list-style: none; font-family: "PT Sans", sans-serif; font-size: 21px; }
  .services li { height: 37px; line-height: 37px; }
  .services li::before { content: "* "; }
</style>
</head>
<body>
<main class="canvas">

  <section class="card card-front">
    <svg class="sweep" viewBox="0 0 700 410" aria-hidden="true">
      <defs>
        <linearGradient id="swooshShade" x1="0" y1="1" x2="1" y2="0">
          <stop offset="0" stop-color="#000"/>
          <stop offset="0.6" stop-color="#4d4d4f"/>
          <stop offset="1" stop-color="#6d6d6f"/>
        </linearGradient>
        <linearGradient id="fieldGreen" x1="0" y1="1" x2="1" y2="0">
          <stop offset="0" stop-color="#2fb34a"/>
          <stop offset="0.5" stop-color="#6cc04a"/>
          <stop offset="1" stop-color="#3bb44a"/>
        </linearGradient>
      </defs>
      <path class="swoosh" d="M0,372 Q165,240 655,236 Q220,262 22,410 L0,410 Z" fill="url(#swooshShade)"/>
      <path class="field" d="M46,410 Q200,250 700,245 L700,410 Z" fill="url(#fieldGreen)"/>
    </svg>

    <div class="identity">
      <div class="name">Tessa Quill</div>
      <div class="role">Director</div>
    </div>

    <ul class="contacts">
      <li>
        <svg viewBox="0 0 18 18" aria-hidden="true"><rect x="3" y="1" width="12" height="16" rx="2" fill="#111"/><rect x="5" y="3.5" width="8" height="10" fill="#6cc04a"/></svg>
        0438 276 615
      </li>
      <li>
        <svg viewBox="0 0 18 18" aria-hidden="true"><path d="M1,7 L9,2 L17,7 L17,16 L1,16 Z" fill="#111"/><path d="M3,8 L9,12 L15,8" fill="none" stroke="#6cc04a" stroke-width="1.6"/></svg>
        tessa@velorahomeworks.com.au
      </li>
      <li>
        <svg viewBox="0 0 18 18" aria-hidden="true"><path d="M3,15 L12,6 M6,4 L14,4 L14,12" fill="none" stroke="#111" stroke-width="3"/></svg>
        www.velorahomeworks.com.au
      </li>
    </ul>
  </section>

  <section class="card card-back">
    <div class="services">
      <h2>Services Offered:</h2>
      <ul>
        <li>Personal Assistant Concierge</li>
        <li>Decluttering Concierge</li>
        <li>Home Management Concierge</li>
        <li>FIFO Concierge</li>
        <li>Events Concierge</li>
        <li>Leisure &amp; Travel Concierge</li>
        <li>Seasonal Concierge</li>
        <li>Professional Concierge</li>
      </ul>
    </div>
  </section>

</main>
</body>
</html>
```